tobrin family medicine business cards

create business cards for 7 family medicine providers and 4 admin using attached logo
2 locations
appointment reminder on back of cards
will provide more info regarding names,addresses, credentials etc once started

```html
<!DOCTYPE html>
<html lang="en">
<head>
<meta charset="utf-8">
<title>Tobrin Family Medicine – Business Card</title>
<link href="https://fonts.googleapis.com/css2?family=Cinzel:wght@700&family=Arimo:wght@400&display=swap" rel="stylesheet">
<style>
  :root{
    --navy:#262468;
    --sky:#29a3db;
    --ink:#333333;
    --rule:#555555;
    --page:#e6e6e6;
    --card:#ffffff;
  }
  html,body{margin:0;padding:0;width:1200px;height:1200px;overflow:hidden;background:var(--page);}
  .card{position:absolute;left:254px;width:692px;height:400px;background:var(--card);overflow:hidden;}
  .card--front{top:160px;}
  .card--back{top:648px;}
  .serif{font-family:"Cinzel",Georgia,serif;font-weight:700;color:var(--navy);}
  .sans{font-family:"Arimo",Arial,sans-serif;color:var(--ink);}

  .lead-name{position:absolute;left:45px;top:42px;margin:0;font-size:25px;letter-spacing:0.2px;}
  .provider-list{position:absolute;left:45px;top:78px;margin:0;padding:0;list-style:none;}
  .provider-list li{height:24.8px;display:flex;align-items:center;font-size:15.5px;}
  .check{width:13px;height:13px;border:1.6px solid var(--navy);border-radius:3px;margin-right:17px;box-sizing:border-box;}

  .brand{position:absolute;right:50px;top:58px;width:250px;text-align:center;}
  .brand-dot{width:78px;height:78px;border-radius:50%;background:var(--sky);margin:0 auto 30px;}
  .brand-name{margin:0;font-size:40px;line-height:1;}
  .brand-sub{margin:10px 0 0;font-size:13px;letter-spacing:8px;}

  .divider{position:absolute;left:45px;top:232px;width:592px;height:0;border-top:1.5px solid var(--rule);}
  .site{position:absolute;font-size:16.5px;line-height:21px;}
  .site--left{left:47px;top:243px;}
  .site--right{right:50px;top:240px;text-align:right;}
  .site p{margin:0;}
  .contact{margin-top:9px !important;}
  .line{display:flex;align-items:center;gap:7px;}
  .site--right .line{justify-content:flex-end;}
  .line svg{width:15px;height:15px;fill:var(--navy);}

  .band{position:absolute;left:0;bottom:0;width:692px;height:48px;}
  .web{position:absolute;left:46px;top:360px;display:flex;align-items:center;gap:7px;font-size:17px;color:#fff;}
  .web svg{width:17px;height:17px;}

  .watermark{position:absolute;left:208px;top:101px;width:222px;height:222px;border-radius:50%;background:#dff0fa;opacity:.7;}
  .back-title{position:absolute;left:0;right:0;top:46px;margin:0;text-align:center;font-size:21.5px;letter-spacing:2.2px;}
  .field{position:absolute;left:48px;right:52px;display:flex;align-items:flex-end;font-size:15px;}
  .field .label{white-space:nowrap;margin-right:5px;}
  .field .fill{flex:1;border-bottom:1.3px dotted var(--navy);margin-bottom:4px;}
  .field--name{top:117px;}
  .field--date{top:178px;left:54px;}
  .field--time{top:248px;left:53px;right:57px;}
  .notice{position:absolute;left:0;right:0;top:325px;margin:0;text-align:center;font-size:15.5px;color:var(--sky);}
</style>
</head>
<body>

<section class="card card--front">
  <h1 class="lead-name serif">Dr. Martin Tobrin, D.O.</h1>
  <ul class="provider-list serif">
    <li><span class="check"></span>Dr. Helen Tobrin, DNP</li>
    <li><span class="check"></span>Dr. Laura Finch, DNP</li>
    <li><span class="check"></span>Renee Alcott, APRN</li>
    <li><span class="check"></span>Dr. Victoria Marlowe, DNP</li>
    <li><span class="check"></span>Denise Holloway, APRN</li>
    <li><span class="check"></span>Dr. Patricia Wendell, MD</li>
  </ul>

  <div class="brand">
    <div class="brand-dot"></div>
    <p class="brand-name serif">TOBRIN</p>
    <p class="brand-sub serif">FAMILY MEDICINE</p>
  </div>

  <div class="divider"></div>

  <div class="site site--left sans">
    <p>4120 Harbor Rd., #210</p>
    <p>Millbrook, FL 33020</p>
    <p class="line contact"><svg viewBox="0 0 24 24"><path d="M6.6 10.8c1.4 2.8 3.8 5.1 6.6 6.6l2.2-2.2c.3-.3.7-.4 1-.2 1.1.4 2.3.6 3.6.6.6 0 1 .4 1 1V20c0 .6-.4 1-1 1C10.6 21 3 13.4 3 4c0-.6.4-1 1-1h3.5c.6 0 1 .4 1 1 0 1.3.2 2.5.6 3.6.1.3 0 .7-.2 1L6.6 10.8z"/></svg>555-210-4471</p>
    <p class="line"><svg viewBox="0 0 24 24"><path d="M6 2h10l2 2v5H6z M3 10h18v9H3z M6 14h12v8H6z" /></svg>555-210-4472</p>
  </div>

  <div class="site site--right sans">
    <p>1850 Lakeview Pkwy #105</p>
    <p>Fairhaven, FL 33041</p>
    <p class="line contact">555-318-6620<svg viewBox="0 0 24 24"><path d="M6.6 10.8c1.4 2.8 3.8 5.1 6.6 6.6l2.2-2.2c.3-.3.7-.4 1-.2 1.1.4 2.3.6 3.6.6.6 0 1 .4 1 1V20c0 .6-.4 1-1 1C10.6 21 3 13.4 3 4c0-.6.4-1 1-1h3.5c.6 0 1 .4 1 1 0 1.3.2 2.5.6 3.6.1.3 0 .7-.2 1L6.6 10.8z"/></svg></p>
    <p class="line">555-318-6621<svg viewBox="0 0 24 24"><path d="M6 2h10l2 2v5H6z M3 10h18v9H3z M6 14h12v8H6z"/></svg></p>
    <p class="line">office@doctortobrin.com<svg viewBox="0 0 24 24"><path d="M2 5h20v14H2z" /><path d="M2 5l10 8 10-8" fill="none" stroke="#fff" stroke-width="1.8"/></svg></p>
  </div>

  <svg class="band" viewBox="0 0 692 48" preserveAspectRatio="none">
    <rect x="0" y="19" width="692" height="29" fill="#29a3db"/>
    <polygon points="0,0 262,0 272,19 0,19" fill="#29a3db"/>
    <polygon points="266,2 692,2 692,15 278,15" fill="#262468"/>
  </svg>
  <div class="web sans">
    <svg viewBox="0 0 24 24" fill="none" stroke="#fff" stroke-width="1.6"><circle cx="12" cy="12" r="10"/><ellipse cx="12" cy="12" rx="4.5" ry="10"/><path d="M2 12h20M4 7h16M4 17h16"/></svg>
    <span>DOCTORTOBRIN.COM</span>
  </div>
</section>

<section class="card card--back">
  <div class="watermark"></div>
  <h2 class="back-title serif">YOUR NEXT APPOINTMENT IS SCHEDULED FOR</h2>
  <div class="field field--name serif"><span class="label">NAME :</span><span class="fill"></span></div>
  <div class="field field--date serif"><span class="label">DATE :</span><span class="fill"></span></div>
  <div class="field field--time serif"><span class="label">TIME :</span><span class="fill"></span></div>
  <p class="notice sans">Please give 24 hours notice for cancellations to avoid a $50.00 no show fee.</p>
</section>

</body>
</html>
```